Design of two graphics from basic existing design & colours

I have two graphics which I currently use but they are nothing special. We would like to transform these two graphics, using our existing logo colour, into something special. The outputs will be used:

- on our website;
- in a powerpoint sales presentation;
- in email campaigns; and
- to print for handing to prospects at the end of a sales presentation.

Please just submit one of the graphics and if we like the design, we will ask you to work on the second graphic. These two graphics are critical to our marketing and will be used together so we need them to have a similar look and feel.

```html
<!DOCTYPE html>
<html lang="en">
<head>
<meta charset="utf-8">
<title>Business Pillars</title>
<link href="https://fonts.googleapis.com/css2?family=Open+Sans:wght@300;400;700;800&display=swap" rel="stylesheet">
<style>
  :root {
    --bg-start: #b1b1b1;
    --bg-end: #e8e8e8;
    --red-bright: #e31e24;
    --red: #a80000;
    --red-deep: #6b1200;
    --red-darkest: #450000;
    --fold-dark: #4a0a00;
    --text: #ffffff;
  }
  * { box-sizing: border-box; margin: 0; padding: 0; }
  html, body { width: 1200px; height: 850px; overflow: hidden; }
  body {
    font-family: "Open Sans", sans-serif;
    background: linear-gradient(150deg, var(--bg-start) 0%, var(--bg-end) 100%);
    position: relative;
    color: var(--text);
  }
  .pillar {
    position: absolute;
    width: 350px;
  }
  .pillar__body {
    position: absolute;
    left: 14px; right: 14px; top: 40px; bottom: 0;
    border-radius: 0 0 8px 8px;
    background: var(--body);
  }
  .pillar__header {
    position: absolute;
    left: 0; top: 0;
    width: 350px; height: 100px;
    overflow: visible;
  }
  .pillar__header .flap { fill: var(--head); }
  .pillar__header .fold { fill: var(--fold-dark); }
  .pillar__header .edge { fill: none; stroke: var(--edge); stroke-width: 3; }
  .pillar__title {
    position: absolute;
    left: 0; right: 0; top: 12px;
    text-align: center;
    font-weight: 800;
    font-size: 32px;
    line-height: 44px;
    letter-spacing: 0.3px;
  }
  .pillar__list {
    position: absolute;
    list-style: none;
    font-weight: 300;
    font-size: 18px;
    line-height: var(--row);
  }
  .pillar__list li::before {
    content: "»";
    font-weight: 700;
    margin-right: 4px;
  }

  .pillar--financial { left: 58px; top: 202px; height: 286px;
    --head: var(--red); --body: var(--red-bright); --edge: var(--red-deep); --row: 30px; }
  .pillar--strategic { left: 425px; top: 133px; height: 286px;
    --head: var(--red-darkest); --body: var(--red-deep); --edge: var(--red); --row: 26px; }
  .pillar--cultural { left: 425px; top: 430px; height: 286px;
    --head: var(--red-darkest); --body: var(--red-deep); --edge: var(--red); --row: 28px; }
  .pillar--operational { left: 791px; top: 202px; height: 286px;
    --head: var(--red-deep); --body: var(--red); --edge: var(--red-bright); --row: 29px; }

  .pillar--financial .pillar__title { top: 14px; }
  .pillar--cultural .pillar__title { top: 17px; }

  .pillar--financial .col-a { left: 59px; top: 117px; }
  .pillar--financial .col-b { left: 190px; top: 117px; }
  .pillar--strategic .col-a { left: 69px; top: 126px; }
  .pillar--strategic .col-b { left: 195px; top: 126px; }
  .pillar--cultural .col-a { left: 43px; top: 114px; }
  .pillar--cultural .col-b { left: 196px; top: 114px; }
  .pillar--operational .col-a { left: 57px; top: 117px; }
  .pillar--operational .col-b { left: 206px; top: 117px; }
</style>
</head>
<body>

<section class="pillar pillar--financial">
  <div class="pillar__body"></div>
  <svg class="pillar__header" viewBox="0 0 350 100" aria-hidden="true">
    <polygon class="fold" points="0,54 14,58 14,70"/>
    <polygon class="fold" points="350,54 336,58 336,70"/>
    <polygon class="flap" points="0,0 350,0 350,54 175,96 0,54"/>
    <polyline class="edge" points="0,54 175,96 350,54"/>
  </svg>
  <h2 class="pillar__title">Financial</h2>
  <ul class="pillar__list col-a"><li>Budget</li><li>CAPEX</li><li>Cash Flow</li></ul>
  <ul class="pillar__list col-b"><li>Delegations</li><li>OPEX</li></ul>
</section>

<section class="pillar pillar--strategic">
  <div class="pillar__body"></div>
  <svg class="pillar__header" viewBox="0 0 350 100" aria-hidden="true">
    <polygon class="fold" points="0,54 14,58 14,70"/>
    <polygon class="fold" points="350,54 336,58 336,70"/>
    <polygon class="flap" points="0,0 350,0 350,54 175,96 0,54"/>
    <polyline class="edge" points="0,54 175,96 350,54"/>
  </svg>
  <h2 class="pillar__title">Strategic</h2>
  <ul class="pillar__list col-a"><li>Board</li><li>Purpose</li><li>Risk</li><li>Strategy</li></ul>
  <ul class="pillar__list col-b"><li>Structure</li><li>Values</li><li>Vision</li></ul>
</section>

<section class="pillar pillar--cultural">
  <div class="pillar__body"></div>
  <svg class="pillar__header" viewBox="0 0 350 100" aria-hidden="true">
    <polygon class="fold" points="0,54 14,58 14,70"/>
    <polygon class="fold" points="350,54 336,58 336,70"/>
    <polygon class="flap" points="0,0 350,0 350,54 175,96 0,54"/>
    <polyline class="edge" points="0,54 175,96 350,54"/>
  </svg>
  <h2 class="pillar__title">Cultural</h2>
  <ul class="pillar__list col-a"><li>Coaching</li><li>Communication</li><li>Competencies</li><li>Development</li><li>Employment</li></ul>
  <ul class="pillar__list col-b"><li>Leadership</li><li>Performance</li><li>Profiles</li><li>Succession</li><li>Teams</li></ul>
</section>

<section class="pillar pillar--operational">
  <div class="pillar__body"></div>
  <svg class="pillar__header" viewBox="0 0 350 100" aria-hidden="true">
    <polygon class="fold" points="0,54 14,58 14,70"/>
    <polygon class="fold" points="350,54 336,58 336,70"/>
    <polygon class="flap" points="0,0 350,0 350,54 175,96 0,54"/>
    <polyline class="edge" points="0,54 175,96 350,54"/>
  </svg>
  <h2 class="pillar__title">Operational</h2>
  <ul class="pillar__list col-a"><li>Competitor</li><li>Compliance</li><li>Customer</li><li>Marketing</li><li>Meetings</li></ul>
  <ul class="pillar__list col-b"><li>Planning</li><li>Policy</li><li>Projects</li><li>Reporting</li><li>Review</li></ul>
</section>

</body>
</html>
```